UI/UX Re-Do for Velmora - a free to use project management platform for desktop and mobile.

UI/UX Re-Do for Velmora
Velmora is a free to use project management platform for desktop and mobile.
We are looking for help with our UI/UX re-design.
As of now the platform is totally functional.
The problem is around flow and look. We want VM to become something that any one can use to manage and even socialize any project. A project can be something work related like organizing a team around a software build, marketing campaign, shared client file space, etc... In fact, most of our current members are using VM for just such work projects.
We also see a project as planning a wedding, organizing a group trip, a simple to-do list, organizing a kids sports team, and so on...
To become a platform that people will use in their work and personal life we first need to become more intuitive and friendly - while maintaining advanced functionality for more advanced needs.
We need help to beautify, streamline, and simplify - while keeping all the functions.
The quickest way to understand VM, and our current issues is this short video:
https://vidshare-example.net/Kq8TzRw2mLp
For sure see this link for the entire most recent description AND images:
https://velmoraapp-example.com/?p=HtrwN4YcZsD
The best way to understand VM is to actually use it:
https://velmoraapp-example.com
Should you choose to take a run at improving VM here are the details:
Please focus your ideas for mobile, it's where we have the biggest issues.
Feel free to get outside the box.
Avoid swipe oriented designs.
Feel free to focus on ideas over polished outputs.
Use any tool you like, PS, hand drawing, written description if you think that works best.
(FYI - we use mostly use Google Presentation docs internally)
Point is illustration of ideas over tool choice.
Feel free to:
Create something totally new
And/or riff on what we have now
And/or riff on the new design we are considering (see images below)
|||
If we go the direction of the images/designs below the idea is to give people options on how they see/experience VM.
Just below is what we are calling Base Mode. This is a more basic and simple flow. Probably a default to keep new users feeling comfortable at the start.
<img src="https://img.picvault-example.net/8tqWLbN.jpg" style="width: 100%;">
https://img.picvault-example.net/8tqWLbN.jpg
|||
We are calling this optional view Atlas Mode. It is more advanced and can show all project, goal(renamed 'milestones') at the same time. This is more of a paint job on the current design.
<img src="https://img.picvault-example.net/mvdHRsJ.jpg" style="width: 100%;">
https://img.picvault-example.net/mvdHRsJ.jpg
|||
If you're submitting please let us know if you can also do the PS files for dev.
Not required, but once we nail down the concepts we want someone to hone in the PS files.
As an optional bonus we will also be giving credit to you/your company in VM.
Let us know if you do or don't want that.
We are excited to see your work!!
<img src=" " style="width: 100%;">
Target Market(s)
Anyone who needs to organize any project, big or small. The key is to make a super friendly user experience for new users while retaining advanced functions.

```html
<!DOCTYPE html>
<html lang="en">
<head>
<meta charset="utf-8">
<title>Velmora – Join Project</title>
<link rel="stylesheet" href="https://fonts.googleapis.com/css2?family=Poppins:wght@300;400;500&display=swap">
<style>
  :root{
    --sidebar:#5a5a5a;
    --main:#4c4c4c;
    --card:#545454;
    --card-line:#4a4a4a;
    --topbar:#1f4bb4;
    --topbar-text:#8fa5d8;
    --brand-dim:#8e3c3c;
    --text-dim:#2b2b2b;
    --text-mid:#333;
    --link-dim:#1d3f8c;
    --green-dim:#1f7a3c;
    --red-dim:#8e3434;
    --modal:#ffffff;
    --ink:#444;
    --muted:#8a8a8a;
    --accent:#3b7cff;
    --danger:#ea4c4c;
    --tick:#3cc25a;
  }
  *{box-sizing:border-box;margin:0;padding:0}
  html,body{width:1200px;height:877px;overflow:hidden}
  body{position:relative;background:var(--main);font-family:'Poppins',sans-serif;font-weight:300}
  .abs{position:absolute}

  .sidebar{left:0;top:0;width:234px;height:877px;background:var(--sidebar)}
  .logo{left:30px;top:20px;font-size:18px;font-weight:500;color:var(--brand-dim)}
  .burger{left:197px;top:25px;width:20px}
  .burger span{display:block;height:2px;background:#222;margin-bottom:5px}
  .avatar{left:62px;top:79px;width:108px;height:108px;border-radius:50%;background:radial-gradient(circle at 50% 40%,#4a4a4a,#2c2c2c)}
  .user{left:0;width:234px;top:198px;text-align:center;font-size:19px;color:var(--text-dim)}
  .nav-mark{left:0;top:293px;width:4px;height:31px;background:var(--red-dim)}
  .nav-item{left:30px;font-size:12.5px;color:var(--text-dim);display:flex;align-items:center;gap:12px}
  .nav-item svg{width:16px;height:16px}
  .nav-item.active{font-weight:500;color:#1f1f1f}
  .caret{left:204px;top:306px}
  .footer{left:43px;top:838px;font-size:12.5px;color:var(--text-dim)}

  .topbar{left:234px;top:0;width:966px;height:60px;background:var(--topbar)}
  .search{left:278px;top:19px;display:flex;align-items:center;gap:10px;font-size:11.5px;color:var(--topbar-text)}
  .topbar-sep{left:1064px;top:0;width:1px;height:60px;background:#1a3f99}

  .card{background:var(--card)}
  .picks{left:278px;top:105px;width:341px;height:772px}
  .picks-head{left:296px;top:123px;font-size:15px;color:var(--red-dim)}
  .picks-line{left:278px;top:159px;width:341px;height:1px;background:var(--card-line)}
  .item{left:296px;top:204px;width:306px;height:48px;border:1px solid var(--card-line);border-left:2px solid var(--red-dim)}
  .item-title{left:310px;top:213px;font-size:12.5px;color:var(--text-dim)}
  .item-sub{left:310px;top:233px;font-size:8px;color:#474747}
  .row{left:296px;font-size:14.5px;color:var(--text-dim);width:306px;display:flex;justify-content:space-between;align-items:center}
  .row-line{left:278px;width:341px;height:1px;background:var(--card-line)}

  .post{left:665px;top:105px;width:491px;height:568px}
  .post-avatar{left:704px;top:150px;width:40px;height:40px;border-radius:50%;background:var(--green-dim);color:#2d9c52;font-size:14px;font-weight:500;display:flex;align-items:center;justify-content:center}
  .post-title{left:757px;top:148px;font-size:16px;color:var(--text-dim)}
  .post-date{left:757px;top:173px;font-size:10.5px;color:#353535}
  .notes{left:1055px;top:162px;font-size:11px;color:var(--text-dim);text-decoration:underline}
  .post-text{font-size:12.5px;color:var(--text-mid);white-space:nowrap}
  .post-link{color:var(--link-dim)}
  .compose{left:665px;top:698px;width:491px;height:53px}
  .compose-text{left:684px;top:715px;font-size:13.5px;color:var(--text-dim)}

  .frame{left:209px;top:230px;width:782px;height:417px;background:rgba(255,255,255,.12)}
  .modal{left:233px;top:254px;width:734px;height:369px;background:var(--modal)}
  .modal-lead{left:273px;top:280px;font-size:15.5px;font-weight:400;color:var(--ink)}
  .modal-line{left:273px;top:328px;width:654px;height:1px;background:#e4e4e4}
  .modal-title{left:272px;top:392px;font-size:38px;font-weight:400;color:var(--accent);letter-spacing:.3px}
  .modal-sub{left:273px;top:460px;font-size:14px;color:var(--muted)}
  .check{left:273px;display:flex;align-items:center;gap:8px;font-size:12.5px;color:var(--muted)}
  .box{width:12px;height:12px;border-radius:2px;background:#ececec;display:flex;align-items:center;justify-content:center}
  .box.on{background:var(--tick)}
  .close{left:824px;top:546px;width:96px;height:39px;background:var(--danger);color:#fff;font-size:11px;font-weight:400;display:flex;align-items:center;justify-content:center}
</style>
</head>
<body>

<aside class="sidebar abs">
  <div class="logo abs">Velmora</div>
  <div class="burger abs"><span></span><span></span><span></span></div>
  <div class="avatar abs" role="img" aria-label="Profile photo of the signed-in user"></div>
  <div class="user abs">Marla Quinten</div>

  <div class="nav-mark abs"></div>
  <div class="nav-item active abs" style="top:301px">
    <svg viewBox="0 0 16 16"><rect x="1" y="2" width="14" height="9" fill="none" stroke="#222" stroke-width="1.4"/><path d="M5 14h6M8 11v3" stroke="#222" stroke-width="1.4"/></svg>My Projects</div>
  <svg class="caret abs" width="10" height="8" viewBox="0 0 10 8"><path d="M1 2l4 4 4-4" fill="none" stroke="var(--red-dim)" stroke-width="1.6"/></svg>
  <div class="nav-item abs" style="top:346px">
    <svg viewBox="0 0 16 16"><circle cx="5" cy="5" r="2.5" fill="#222"/><circle cx="11" cy="5" r="2.5" fill="#222"/><path d="M0 14c0-4 10-4 10 0zM6 14c0-4 10-4 10 0z" fill="#222"/></svg>Public Projects</div>
  <div class="nav-item abs" style="top:391px">
    <svg viewBox="0 0 16 16"><circle cx="8" cy="8" r="5" fill="none" stroke="#222" stroke-width="3" stroke-dasharray="2.4 1.5"/><circle cx="8" cy="8" r="2" fill="#222"/></svg>Admin</div>
  <div class="nav-item abs" style="top:436px">
    <svg viewBox="0 0 16 16"><path d="M7 2H2v12h5" fill="none" stroke="#222" stroke-width="1.5"/><path d="M6 8h8M11 5l3 3-3 3" fill="none" stroke="#222" stroke-width="1.5"/></svg>Sign Out</div>
  <div class="nav-item abs" style="top:482px">
    <svg viewBox="0 0 16 16"><circle cx="8" cy="8" r="6" fill="#222"/><path d="M8 7v4" stroke="#5a5a5a" stroke-width="1.6"/><circle cx="8" cy="5" r="1" fill="#5a5a5a"/></svg>About Velmora</div>
  <div class="nav-item abs" style="top:527px">
    <svg viewBox="0 0 16 16"><path d="M3 1h7l3 3v11H3z" fill="none" stroke="#222" stroke-width="1.4"/><path d="M5 7h6M5 10h6" stroke="#222" stroke-width="1.2"/></svg>Terms and Condition</div>

  <div class="footer abs">© 2017 All Rights Reserved</div>
</aside>

<header class="topbar abs"></header>
<div class="search abs">
  <svg width="22" height="22" viewBox="0 0 22 22"><circle cx="9" cy="9" r="7" fill="none" stroke="#7e95cc" stroke-width="2"/><path d="M14 14l6 6" stroke="#7e95cc" stroke-width="2"/></svg>
  <span>Search revenue here...</span>
</div>
<div class="topbar-sep abs"></div>
<svg class="abs" style="left:1089px;top:22px" width="24" height="16" viewBox="0 0 24 16"><rect x="0" y="0" width="3" height="16" fill="#1b3f99"/><rect x="5" y="2" width="19" height="12" fill="#1b3f99"/></svg>
<svg class="abs" style="left:1127px;top:17px" width="29" height="25" viewBox="0 0 29 25"><rect width="29" height="25" fill="#9aa6bf"/><rect x="6" y="4" width="3" height="17" fill="#2a2a2a"/><rect x="13" y="4" width="3" height="17" fill="#2a2a2a"/><rect x="20" y="4" width="3" height="17" fill="#2a2a2a"/></svg>

<section class="picks card abs"></section>
<div class="picks-head abs">Velmora Top Projects Picks</div>
<svg class="abs" style="left:591px;top:130px" width="12" height="9" viewBox="0 0 12 9"><path d="M1 2l5 5 5-5" fill="none" stroke="var(--red-dim)" stroke-width="2"/></svg>
<div class="picks-line abs"></div>
<div class="item abs"></div>
<div class="item-title abs">Startup starter Kit</div>
<div class="item-sub abs">Status</div>
<div class="row abs" style="top:673px"><span>Most Popular Public Projects</span><svg width="8" height="12" viewBox="0 0 8 12"><path d="M1 1l5 5-5 5" fill="none" stroke="#2a2a2a" stroke-width="1.8"/></svg></div>
<div class="row-line abs" style="top:709px"></div>
<div class="row abs" style="top:724px"><span>All Public Projects</span><svg width="8" height="12" viewBox="0 0 8 12"><path d="M1 1l5 5-5 5" fill="none" stroke="#2a2a2a" stroke-width="1.8"/></svg></div>

<section class="post card abs"></section>
<div class="post-avatar abs">VM</div>
<div class="post-title abs">Derek Hollis VM Cases</div>
<div class="post-date abs">6/1/2017 6:06 am PKT</div>
<div class="notes abs">Notes</div>
<svg class="abs" style="left:1094px;top:167px" width="8" height="5" viewBox="0 0 8 5"><path d="M0 0h8L4 5z" fill="#2a2a2a"/></svg>
<svg class="abs" style="left:1122px;top:162px" width="4" height="14" viewBox="0 0 4 14"><circle cx="2" cy="2" r="1.6" fill="var(--green-dim)"/><circle cx="2" cy="7" r="1.6" fill="var(--green-dim)"/><circle cx="2" cy="12" r="1.6" fill="var(--green-dim)"/></svg>
<div class="post-text abs" style="left:710px;top:226px">Welcome to the Velmora startuo Kit' do more better!</div>
<div class="post-text abs" style="left:710px;top:270px">Here you will be able to see all the assets and structure in</div>
<div class="post-text abs" style="left:710px;top:295px">place for your new venture. What you will find here are</div>
<div class="post-text abs" style="left:710px;top:320px">tools that help you in the earliest phases.</div>
<div class="post-text abs" style="left:710px;top:457px">Have a look around and let us know if we can help!</div>
<div class="post-text post-link abs" style="left:710px;top:504px">https://vidshare-example.net/Kq8TzRw2mLpHtrwN4YcZsD</div>
<div class="compose card abs"></div>
<div class="compose-text abs">Type here</div>
<svg class="abs" style="left:1040px;top:718px" width="95" height="14" viewBox="0 0 95 14"><g fill="#4a4a4a"><circle cx="7" cy="7" r="6"/><path d="M30 9l6-6 3 3-6 6z"/><rect x="53" y="3" width="13" height="9" rx="1"/><rect x="81" y="1" width="9" height="12" rx="1"/></g></svg>

<div class="frame abs"></div>
<div class="modal abs" role="dialog" aria-label="Join project"></div>
<div class="modal-lead abs">By Joining this Project You Will Be Able To share, Comment &amp; Interact</div>
<div class="modal-line abs"></div>
<h1 class="modal-title abs">Startup Starter Kit</h1>
<div class="modal-sub abs">In Order Alredy Registered with Velmora</div>
<label class="check abs" style="top:510px"><span class="box on"><svg width="8" height="7" viewBox="0 0 8 7"><path d="M1 3.5l2 2 4-4.5" fill="none" stroke="#fff" stroke-width="1.5"/></svg></span>I am Already Registered With Velmora</label>
<label class="check abs" style="top:536px"><span class="box"></span>I am a new User &amp; Want an invite</label>
<div class="close abs">CLOSE</div>

</body>
</html>
```